QuadLantern--Help Us look fresh and new to companies, college students and college career centers!

We just designed a new logo and would like to freshen-up and make our business cards a bit more modern. Not crazy-modern like Velmont, but modern like metro-style and fresh like fruit. We use three logos with a combination of two colors each, and three colors total. We are looking for a single format to apply to three different cards/color schemes (green/blue to give out to companies, orange/green for students, and orange/blue for university career centers). Thanks everyone--looking forward to seeing your designs!!

Target Market(s)

Three styles: companies, college students/grads, college career centers

Industry/Entity Type

College

Contact Information for Business Card

Address: 5718 Harlow Street, Suite 412, Seattle, WA 98109. Need a spot for email address, web address (www.quadlantern.example), and phone numbers (main, direct, mobile). Don't open that website unless you want to lose your lunch--it is waaaay old and outdated. See this link instead, http://preview.mossgrovedev.example/QuadLantern/HiringTools, for our new website design in progress.

Font styles to use
Sans Serif

Requirements
Must have
• Please use the logos supplied. Would like text to be grey but printable, like a "light" type style that is metro-type with sans-serif. NOT black text. Modern. For inspiration, here's a link to our work-in-progress website we are planning to launch soon: http://preview.mossgrovedev.example/QuadLantern/HiringTools
Nice to have
• Would like to see something unique and different in a "metro" style. Clean and not cluttered.
Should not have
• No odd-sized cards

```html
<!DOCTYPE html>
<html lang="en">
<head>
<meta charset="utf-8">
<title>QuadLantern Business Card</title>
<link rel="stylesheet" href="https://fonts.googleapis.com/css2?family=Open+Sans:wght@400;700&display=swap">
<style>
  :root {
    --page-bg: #e9eee2;
    --card-light: #f4f4f3;
    --card-mid: #dcdcda;
    --brand-blue: #1f73ad;
    --brand-green: #8bb935;
    --tile-top: #2e95d0;
    --tile-bottom: #1a7bbd;
    --tile-text: #ffffff;
  }
  * { margin: 0; padding: 0; box-sizing: border-box; }
  html, body { width: 1200px; height: 1200px; overflow: hidden; }
  body {
    background: var(--page-bg);
    display: flex; align-items: center; justify-content: center;
    font-family: "Open Sans", Arial, sans-serif;
  }
  .business-card {
    width: 1000px; height: 572px;
    border-radius: 26px;
    background: linear-gradient(135deg, var(--card-light) 0%, var(--card-mid) 55%, var(--card-light) 100%);
    box-shadow: 0 14px 34px rgba(60, 80, 40, 0.22);
    display: flex; flex-direction: column; align-items: center;
    padding-top: 60px;
  }
  .brand {
    display: flex; align-items: center; gap: 18px;
    margin-bottom: 40px;
  }
  .brand-dot {
    width: 58px; height: 58px; border-radius: 50%;
    background: var(--brand-green);
  }
  .brand-name {
    font-size: 64px; font-weight: 700; letter-spacing: -1px;
    color: var(--brand-blue); line-height: 1;
  }
  .contact-grid {
    display: grid;
    grid-template-columns: 290px 290px;
    grid-template-rows: 158px 158px;
    gap: 16px;
  }
  .contact-tile {
    border-radius: 22px;
    background: linear-gradient(160deg, var(--tile-top), var(--tile-bottom));
    display: flex; flex-direction: column; align-items: center; justify-content: center;
    gap: 14px;
    color: var(--tile-text);
    font-size: 15px; font-weight: 400; text-align: center; line-height: 1.35;
  }
  .contact-icon { width: 34px; height: 34px; }
</style>
</head>
<body>
  <div class="business-card">
    <div class="brand">
      <span class="brand-dot"></span>
      <span class="brand-name">QuadLantern</span>
    </div>
    <div class="contact-grid">
      <div class="contact-tile email">
        <svg class="contact-icon" viewBox="0 0 34 34" aria-hidden="true">
          <circle cx="17" cy="17" r="17" fill="#8bb935"/>
          <rect x="9" y="11" width="16" height="12" rx="1.5" fill="none" stroke="#fff" stroke-width="2"/>
          <path d="M9.5 12 L17 18 L24.5 12" fill="none" stroke="#fff" stroke-width="2"/>
        </svg>
        <span>email@email.com</span>
      </div>
      <div class="contact-tile phone">
        <svg class="contact-icon" viewBox="0 0 34 34" aria-hidden="true">
          <circle cx="17" cy="17" r="17" fill="#8bb935"/>
          <path d="M12 9 L15 9 L16 13 L14 14.5 Q16 19 19.5 20 L21 18 L25 19 L25 22 Q24 25 20 24 Q12 21 10 13 Q10 10 12 9 Z" fill="#fff"/>
        </svg>
        <span>xxx.xxx.xxxx</span>
      </div>
      <div class="contact-tile address">
        <svg class="contact-icon" viewBox="0 0 34 34" aria-hidden="true">
          <circle cx="17" cy="17" r="17" fill="#8bb935"/>
          <path d="M17 8 C12.5 8 11 11.5 11 14 C11 18 17 26 17 26 C17 26 23 18 23 14 C23 11.5 21.5 8 17 8 Z" fill="#fff"/>
          <circle cx="17" cy="14" r="2.4" fill="#8bb935"/>
        </svg>
        <span>5718 Harlow Street, Suite 412,<br>Seattle, WA 98109</span>
      </div>
      <div class="contact-tile website">
        <svg class="contact-icon" viewBox="0 0 34 34" aria-hidden="true">
          <circle cx="17" cy="17" r="17" fill="#8bb935"/>
          <circle cx="17" cy="17" r="8" fill="none" stroke="#fff" stroke-width="1.8"/>
          <ellipse cx="17" cy="17" rx="3.5" ry="8" fill="none" stroke="#fff" stroke-width="1.5"/>
          <line x1="9" y1="17" x2="25" y2="17" stroke="#fff" stroke-width="1.5"/>
        </svg>
        <span>www.quadlantern.example</span>
      </div>
    </div>
  </div>
</body>
</html>
```